Kestrel Calisthenics Gym Website

We need a website design for our gym.

Kestrel is the UAE's first calisthenics and parkour gym. The theme under which the gym revolves is that one does not require any machinery to workout as our bodies could be themselves the machinery. The gym is designed to be the more of a social hub rather than an "in-and-out" gym, where people come train, have fun, hang out and socialize for a few hours rather than just train for 60 minutes then leave. The gym is designed to be a big open space with lots of natural sunlight, natural wood and plants all over the place to create a natural and refreshing setting. We also use recycled material throughout the gym and recycle our waste as being green is part of our philosophy. We currently also have some of the world's top and most recognized calisthenics athletes working with us.

We would like our website to reflect all that as well as provide a simple, interactive and fun way for visitors to be able to get class and gym information, check out gym media and contact us for bookings.

Target Market(s)

Ages 15-35

Industry/Entity Type

Fitness

Coding

Coded - Design and coding required

Number of Pages Required

4 page

Font styles to use
Decorative

Colors
0792cd

Requirements
Must have
• Class descriptions
• Gym description
• Class schedules
• Trainer profiles
• Gym philosophy
• Contact Details
Nice to have
• A link to contact us directly for a free first trial class

```html
<!DOCTYPE html>
<html lang="en">
<head>
<meta charset="utf-8">
<title>Kestrel Calisthenics Gym – Trainer profiles</title>
<link rel="stylesheet" href="https://fonts.googleapis.com/css2?family=Open+Sans:wght@300;400;600;700&display=swap">
<style>
  :root{
    --stage:#dfe3e6;
    --teal:#2cbccb;
    --blue:#0792cd;
    --blue-deep:#1878b8;
    --nav-active:#0a84b6;
    --header-dark:#1f2124;
    --orange-a:#dc6f0e;
    --orange-b:#f2b424;
    --ink:#2b2f33;
    --accent:#1a9ad0;
    --muted:#555b60;
    --white:#ffffff;
  }
  *{box-sizing:border-box;margin:0;padding:0}
  html,body{width:1200px;height:816px;overflow:hidden;background:var(--stage);font-family:"Open Sans",Arial,sans-serif}
  .site{position:absolute;left:134px;top:0;width:960px;height:840px;transform:scale(.9714);transform-origin:0 0;overflow:hidden;box-shadow:0 6px 30px rgba(0,0,0,.25)}

  .sidebar{position:absolute;left:0;top:0;width:218px;height:840px;
    background:linear-gradient(180deg,var(--teal) 0%,#2ab3cc 30%,#1b9fd2 50%,var(--blue-deep) 62%,#23a8c6 82%,var(--teal) 100%);color:var(--white)}
  .brand{position:absolute;left:43px;top:21px;width:132px;height:132px;border-radius:50%;background:var(--white);
    display:flex;align-items:center;justify-content:center;font-weight:700;font-size:25px;color:var(--blue-deep)}
  .nav{position:absolute;top:174px;left:0;width:218px;list-style:none}
  .nav li{height:39.5px;display:flex;align-items:center;padding-left:48px;font-size:14.5px;position:relative;border-top:1px solid rgba(255,255,255,.12)}
  .nav li svg{position:absolute;left:17px;top:50%;transform:translateY(-50%)}
  .nav li.active{background:var(--nav-active);height:42px}
  .contact{position:absolute;right:26px;top:689px;text-align:right;font-size:11.5px;line-height:14px}
  .contact p{margin-bottom:12px}
  .map-btn{position:absolute;left:25px;top:790px;width:166px;height:32px;border:1.5px solid var(--white);border-radius:16px;
    display:flex;align-items:center;justify-content:center;font-size:12px;color:var(--white)}

  .header{position:absolute;left:218px;top:0;width:742px;height:174px;background:linear-gradient(100deg,#151618,#3a3d40 45%,#1d1f22)}
  .trial{position:absolute;left:250px;top:47px;width:434px;height:82px;border:1px solid rgba(255,255,255,.25);border-radius:41px}
  .trial span{position:absolute;left:38px;top:28px;font-size:18px;color:var(--white)}
  .cta{position:absolute;left:230px;top:7px;width:195px;height:66px;border-radius:33px;
    background:linear-gradient(90deg,var(--orange-a),var(--orange-b));display:flex;align-items:center;justify-content:center;
    font-size:24px;font-weight:300;color:var(--white)}

  .profile{position:absolute;left:218px;top:174px;width:742px;height:295px;background:linear-gradient(90deg,#f4f8fa 0%,#e3eef3 45%,#b9c9d0 100%)}
  .profile .photo{position:absolute;right:0;top:0;width:330px;height:295px;background:linear-gradient(90deg,rgba(200,210,214,0),#a9a090 40%,#c9a58a 75%,#8f8f88)}
  .profile h1{position:absolute;left:39px;top:30px;font-size:30px;font-weight:300;color:var(--ink)}
  .profile .role{position:absolute;left:40px;top:73px;font-size:14px;color:var(--accent)}
  .profile .bio{position:absolute;left:40px;top:106px;width:296px;font-size:9.3px;line-height:12px;color:var(--ink)}
  .profile .bio p+p{margin-top:12px}

  .team{position:absolute;left:218px;top:469px;width:742px;height:371px;background:linear-gradient(100deg,#9ab4c2 0%,#c4ccd0 45%,#cbc6c0 80%,#d4cbc1 100%)}
  .tab{position:absolute;top:13px;font-size:11.5px;color:var(--white);padding-bottom:10px;border-bottom:1px solid rgba(255,255,255,.6)}
  .tab.personal{left:12px;width:345px;padding-left:3px}
  .tab.group{left:359px;width:350px;padding-left:2px;color:#6a7378}
  .scrollbar{position:absolute;left:722px;top:8px;width:8px;height:347px;border-radius:4px;background:rgba(0,0,0,.12)}
  .scrollbar i{display:block;height:260px;border-radius:4px;background:#2a2d30}
  .trainer{position:absolute;width:110px;margin-left:-55px;text-align:center;font-size:13px;line-height:16px;color:var(--muted)}
  .avatar{display:block;width:76px;height:76px;margin:0 auto 9px;border-radius:50%;background:radial-gradient(circle at 50% 40%,#c99b7c,#5b4a40 70%,#2e3032)}
  .avatar.dark{background:radial-gradient(circle at 50% 40%,#8a5e44,#3a2a22 70%,#2a2a2a)}
  .avatar.selected{box-shadow:0 0 0 3px var(--white)}
</style>
</head>
<body>
<div class="site">
  <aside class="sidebar">
    <div class="brand">Kestrel</div>
    <ul class="nav">
      <li><svg width="16" height="15" viewBox="0 0 16 15"><path d="M1.5 7.5 8 1.5l6.5 6" fill="none" stroke="#1a6fb0" stroke-width="1.6" stroke-linejoin="round"/><path d="M3.5 6.5V14h9V6.5" fill="none" stroke="#1a6fb0" stroke-width="1.6"/></svg>About gym</li>
      <li><svg width="18" height="12" viewBox="0 0 18 12"><path d="M1 1h16M1 6h12M1 11h8" stroke="#fff" stroke-width="1.6"/></svg>Class descriptions</li>
      <li><svg width="16" height="16" viewBox="0 0 16 16"><rect x="1" y="2" width="14" height="13" rx="1.5" fill="none" stroke="#1a6fb0" stroke-width="1.6"/><path d="M1 6h14" stroke="#1a6fb0" stroke-width="2"/></svg>Class schedules</li>
      <li class="active"><svg width="14" height="16" viewBox="0 0 14 16"><circle cx="7" cy="4.5" r="3.5" fill="#fff"/><path d="M1 16c0-5 2.5-7 6-7s6 2 6 7z" fill="#fff"/></svg>Trainer profiles</li>
    </ul>
    <div class="contact">
      <p>555 014 27 83</p>
      <p>40210, Harbour Road<br>Unit 7, Hall B</p>
      <p>hello@kestrelgym.com</p>
    </div>
    <div class="map-btn">Show on map</div>
  </aside>

  <header class="header">
    <div class="trial"><span>Free first trial class</span><div class="cta">Contact Us</div></div>
  </header>

  <section class="profile">
    <div class="photo" role="img" aria-label="Portrait photo of the selected trainer in the gym"></div>
    <h1>Leo Marsh</h1>
    <div class="role">personal trainer</div>
    <div class="bio">
      <p>Lorem ipsum dolor sit amet, consectetur adipisicing elit, sed do eiusmod tempor incididunt ut labore et dolore magna aliqua. Ut enim ad minim veniam, quis nostrud exercitation ullamco laboris nisi ut aliquip ex ea commodo consequat. beatae vitae dicta sunt explicabo. Nemo enim ipsam voluptatem quia voluptas sit aspernatur aut aliquam quaerat voluptatem.</p>
      <p>Ut enim ad minim veniam, quis nostrud exercitation ullamco laboris nisi ut aliquip ex ea commodo consequat. beatae vitae dicta sunt explicabo.</p>
    </div>
  </section>

  <section class="team">
    <div class="tab personal">Personal trainers</div>
    <div class="tab group">Group trainers</div>
    <div class="scrollbar"><i></i></div>

    <div class="trainer" style="left:73px;top:65px"><span class="avatar selected" role="img" aria-label="Trainer portrait"></span>Leo<br>Marsh</div>
    <div class="trainer" style="left:185px;top:65px"><span class="avatar" role="img" aria-label="Trainer portrait"></span>Omar<br>Reyes</div>
    <div class="trainer" style="left:303px;top:65px"><span class="avatar dark" role="img" aria-label="Trainer portrait"></span>Nadia<br>Cole</div>
    <div class="trainer" style="left:419px;top:65px"><span class="avatar" role="img" aria-label="Trainer portrait"></span>Leo<br>Marsh</div>
    <div class="trainer" style="left:531px;top:65px"><span class="avatar" role="img" aria-label="Trainer portrait"></span>Omar<br>Reyes</div>
    <div class="trainer" style="left:649px;top:65px"><span class="avatar dark" role="img" aria-label="Trainer portrait"></span>Nadia<br>Cole</div>

    <div class="trainer" style="left:73px;top:212px"><span class="avatar" role="img" aria-label="Trainer portrait"></span>Leo<br>Marsh</div>
    <div class="trainer" style="left:185px;top:212px"><span class="avatar" role="img" aria-label="Trainer portrait"></span>Omar<br>Reyes</div>
    <div class="trainer" style="left:303px;top:212px"><span class="avatar dark" role="img" aria-label="Trainer portrait"></span>Nadia<br>Cole</div>
  </section>
</div>
</body>
</html>
```